Consulting firm needs an infographic

The consulting we do needs a very graphic and understandable way to have perspective clients get exactly where we can help their company grow. I designed something that needs a lot of spice for it to look professional and relatable to them. This is being created to be used on a business card, as well as on posters, and social media.

```html
<!DOCTYPE html>
<html lang="en">
<head>
<meta charset="utf-8">
<title>Growth Map Infographic</title>
<link rel="stylesheet" href="https://fonts.googleapis.com/css2?family=Lexend:wght@400;500;600&family=Montserrat:wght@800&display=swap">
<style>
  :root{
    --bg:#eef1f9;
    --bg-center:#f8f9fd;
    --navy:#2f2d6b;
    --white:#ffffff;
    --purple:#5a36e6;
    --blue:#5ea8f6;
    --teal:#3aaee6;
    --green:#2dc36c;
    --yellow:#f4d656;
    --orange:#e4623a;
    --shadow:rgba(70,60,140,.22);
  }
  *{margin:0;padding:0;box-sizing:border-box}
  html,body{width:1200px;height:1200px;overflow:hidden}
  body{
    position:relative;
    background:radial-gradient(circle at 50% 55%,var(--bg-center) 0,var(--bg) 70%);
    font-family:"Lexend",sans-serif;
    color:var(--navy);
  }
  .flows{position:absolute;left:0;top:0;width:1200px;height:1200px}

  .brand{position:absolute;left:32px;top:40px;font-size:22px;line-height:28px;font-weight:500;color:var(--navy)}

  .hub{
    position:absolute;left:388px;top:41px;width:422px;height:422px;border-radius:50%;
    background:var(--white);box-shadow:0 18px 40px var(--shadow);
    text-align:center;
  }
  .hub-title{font-family:"Montserrat",sans-serif;font-weight:800;color:var(--navy);letter-spacing:-1px}
  .hub-title .line1{display:block;font-size:70px;line-height:70px;margin-top:68px}
  .hub-title .line2{display:block;font-size:72px;line-height:72px;margin-top:-4px}
  .hub-sub{font-size:37px;font-weight:400;margin-top:8px;color:var(--navy)}

  .pillar{position:absolute;top:331px;width:174px;text-align:center}
  .pillar-badge{
    width:174px;height:174px;border-radius:50%;background:var(--white);
    box-shadow:0 14px 30px var(--shadow);
    display:flex;align-items:center;justify-content:center;
  }
  .pillar-art{width:100px;height:90px;border-radius:14px;background:linear-gradient(135deg,#dcdcf2,#c9c8ea)}
  .pillar-label{margin-top:16px;font-size:23px;line-height:30px;font-weight:500;color:var(--navy);margin-left:-20px;margin-right:-20px}
  .p1{left:322px}.p2{left:512px}.p3{left:703px}

  .tag{position:absolute;height:86px;width:300px}
  .tag-bar{position:absolute;left:32px;top:8px;right:12px;height:58px}
  .tag-echo{position:absolute;left:40px;top:18px;right:0;height:58px;opacity:.28}
  .tag-disc{position:absolute;left:0;top:-10px;width:86px;height:86px;border-radius:50%}
  .tag-disc-echo{position:absolute;left:8px;top:0;width:86px;height:86px;border-radius:50%;opacity:.3}
  .tag-icon{position:absolute;left:19px;top:11px;width:48px;height:44px;border-radius:10px;background:rgba(255,255,255,.35)}
  .tag-text{position:absolute;left:90px;top:8px;line-height:58px;font-size:27px;font-weight:500;color:var(--white);white-space:nowrap}
  .tag-text.compact{font-size:25px;letter-spacing:-.3px}

  .supply .tag-bar,.supply .tag-echo{background:linear-gradient(90deg,var(--purple),var(--blue))}
  .supply .tag-disc{background:linear-gradient(135deg,var(--purple),#6f7df0)}
  .supply .tag-disc-echo{background:var(--purple)}
  .ops .tag-bar,.ops .tag-echo{background:linear-gradient(90deg,var(--teal),var(--green))}
  .ops .tag-disc{background:linear-gradient(135deg,var(--teal),#3bb6a6)}
  .ops .tag-disc-echo{background:var(--green)}
  .market .tag-bar,.market .tag-echo{background:linear-gradient(90deg,var(--yellow),var(--orange))}
  .market .tag-disc{background:linear-gradient(135deg,var(--yellow),#eea548)}
  .market .tag-disc-echo{background:var(--orange)}

  .supply{left:19px;width:287px}
  .ops{left:442px;width:319px}
  .market{left:881px;width:305px}
</style>
</head>
<body>

<svg class="flows" viewBox="0 0 1200 1200" aria-hidden="true">
  <defs>
    <linearGradient id="coolFlow" x1="0" y1="0" x2="0" y2="1">
      <stop offset="0" stop-color="#5a36e6"/><stop offset="1" stop-color="#6fb0f7"/>
    </linearGradient>
    <linearGradient id="warmFlow" x1="0" y1="0" x2="1" y2="1">
      <stop offset="0" stop-color="#f4d656"/><stop offset=".5" stop-color="#ea8a40"/><stop offset="1" stop-color="#e4623a"/>
    </linearGradient>
    <linearGradient id="tealFlow" x1="0" y1="0" x2="1" y2="0">
      <stop offset="0" stop-color="#4f7be8"/><stop offset="1" stop-color="#3ab0d0"/>
    </linearGradient>
    <linearGradient id="limeFlow" x1="0" y1="0" x2="1" y2="0">
      <stop offset="0" stop-color="#2dc36c"/><stop offset="1" stop-color="#f4d656"/>
    </linearGradient>
  </defs>

  <g fill="none" stroke="url(#coolFlow)" stroke-linecap="butt" opacity=".92">
    <path d="M398,196 C225,232 72,355 85,602" stroke-width="24"/>
    <path d="M398,236 C262,262 125,392 132,618" stroke-width="14"/>
    <path d="M398,290 C282,318 188,420 198,568" stroke-width="30"/>
  </g>
  <g fill="#6aaaf6">
    <polygon points="52,600 118,600 86,658"/>
    <polygon points="118,614 146,614 132,662"/>
    <polygon points="144,564 246,564 197,660"/>
  </g>

  <g fill="none" stroke="url(#warmFlow)" opacity=".9">
    <path d="M1012,670 C1010,420 960,232 832,198" stroke-width="14"/>
    <path d="M1074,670 C1070,425 965,275 842,250" stroke-width="32"/>
    <path d="M1118,670 C1110,455 1000,322 848,294" stroke-width="22"/>
  </g>
  <g fill="#f2c955">
    <polygon points="812,192 850,180 842,214"/>
    <polygon points="818,246 910,205 880,298"/>
    <polygon points="826,290 872,262 864,316"/>
  </g>

  <g fill="none" stroke="url(#tealFlow)" stroke-width="7">
    <path d="M320,830 C380,830 385,860 420,862"/>
    <path d="M320,845 C380,848 370,905 420,910"/>
    <path d="M320,877 C390,877 380,820 425,815"/>
  </g>
  <g fill="#3ab0d0">
    <polygon points="432,815 416,805 418,826"/>
    <polygon points="428,862 412,852 414,872"/>
    <polygon points="430,911 414,901 416,921"/>
  </g>

  <g fill="none" stroke="url(#limeFlow)" stroke-width="7" opacity=".85">
    <path d="M772,842 C830,845 825,818 866,815"/>
    <path d="M772,857 C830,858 825,853 862,852"/>
    <path d="M772,887 C830,885 830,900 866,900"/>
  </g>
  <g fill="#f4d656">
    <polygon points="878,815 862,805 864,826"/>
    <polygon points="874,852 858,843 860,862"/>
    <polygon points="878,900 862,890 864,911"/>
  </g>

  <g fill="none" stroke-width="4">
    <path d="M598,728 C604,752 620,762 635,772" stroke="#3ab8c8"/>
    <path d="M607,770 C612,752 618,744 620,730" stroke="#2dc36c"/>
    <path d="M596,770 C610,752 612,742 614,730" stroke="#5bc58a"/>
  </g>
</svg>

<div class="brand">Northvale Advisory</div>

<div class="hub">
  <h1 class="hub-title"><span class="line1">Your</span><span class="line2">Company</span></h1>
  <p class="hub-sub">Products/Services</p>
</div>

<div class="pillar p1">
  <div class="pillar-badge"><div class="pillar-art" role="img" aria-label="Icon of a team with a rising growth arrow"></div></div>
  <p class="pillar-label">Content<br>Workforce</p>
</div>
<div class="pillar p2">
  <div class="pillar-badge"><div class="pillar-art" role="img" aria-label="Icon of a process cycle around a gear"></div></div>
  <p class="pillar-label">Productive<br>Workflow</p>
</div>
<div class="pillar p3">
  <div class="pillar-badge"><div class="pillar-art" role="img" aria-label="Icon of colleagues meeting at a table"></div></div>
  <p class="pillar-label">Dynamic<br>Workplace</p>
</div>

<div class="tag supply" style="top:718px"><div class="tag-echo"></div><div class="tag-bar"></div><div class="tag-disc-echo"></div><div class="tag-disc"><div class="tag-icon" role="img" aria-label="Vendor meeting icon"></div></div><span class="tag-text">Vendors</span></div>
<div class="tag supply" style="top:831px"><div class="tag-echo"></div><div class="tag-bar"></div><div class="tag-disc-echo"></div><div class="tag-disc"><div class="tag-icon" role="img" aria-label="Resources gear icon"></div></div><span class="tag-text">Resources</span></div>
<div class="tag supply" style="top:946px"><div class="tag-echo"></div><div class="tag-bar"></div><div class="tag-disc-echo"></div><div class="tag-disc"><div class="tag-icon" role="img" aria-label="Costs calculator icon"></div></div><span class="tag-text">Costs</span></div>

<div class="tag ops" style="top:661px"><div class="tag-echo"></div><div class="tag-bar"></div><div class="tag-disc-echo"></div><div class="tag-disc"><div class="tag-icon" role="img" aria-label="Executive icon"></div></div><span class="tag-text">Executive</span></div>
<div class="tag ops" style="top:773px"><div class="tag-echo"></div><div class="tag-bar"></div><div class="tag-disc-echo"></div><div class="tag-disc"><div class="tag-icon" role="img" aria-label="Administrative network icon"></div></div><span class="tag-text">Administrative</span></div>
<div class="tag ops" style="top:890px"><div class="tag-echo"></div><div class="tag-bar"></div><div class="tag-disc-echo"></div><div class="tag-disc"><div class="tag-icon" role="img" aria-label="Personnel group icon"></div></div><span class="tag-text">Personnel</span></div>
<div class="tag ops" style="top:1010px"><div class="tag-echo"></div><div class="tag-bar"></div><div class="tag-disc-echo"></div><div class="tag-disc"><div class="tag-icon" role="img" aria-label="Delivery truck icon"></div></div><span class="tag-text">Logistics</span></div>

<div class="tag market" style="top:718px"><div class="tag-echo"></div><div class="tag-bar"></div><div class="tag-disc-echo"></div><div class="tag-disc"><div class="tag-icon" role="img" aria-label="Customers icon"></div></div><span class="tag-text">Customers</span></div>
<div class="tag market" style="top:831px"><div class="tag-echo"></div><div class="tag-bar"></div><div class="tag-disc-echo"></div><div class="tag-disc"><div class="tag-icon" role="img" aria-label="Brand identity document icon"></div></div><span class="tag-text compact">Identity &amp; B&amp;M</span></div>
<div class="tag market" style="top:946px"><div class="tag-echo"></div><div class="tag-bar"></div><div class="tag-disc-echo"></div><div class="tag-disc"><div class="tag-icon" role="img" aria-label="Revenue growth chart icon"></div></div><span class="tag-text">Revenue</span></div>

</body>
</html>
```